July 15 Raffle Fundraiser to raise $2000

Fundraiser for the family to travel to Halifax NB and support athlete Corvel Ashbury.
Travel dates: July 16-23,2023

Raffling off three prizes
1) $150.00 Firewood
2) $375.00 Red Safe
3) $300.00 Secure Latch and door knob
4) 20 pieces of frozen coho sockeye

Tickets are
$2.00 each
$5.00 for three

Draw Date: July 15,2023 @11:00am

Please help us raise $2000.00
To alleviate travelling and meal costs
ETransfer: ashburyfundraiser482@plimvex.com

I have included the pervious flyer we used
Information on there as well
And please try keep same Color scheme

Thanks

Target Market(s)

Athlete supporters

Colors

Designer to choose colors to be used in the design.

Requirements
Must have
• Pictures of the raffle items , with exception of the fish there no picture of fish
Nice to have
• Pictures of the athlete in a minimal way. Similar to the colours and design of previous flyer to stay consistent. But fine if it is different.

```html
<!DOCTYPE html>
<html lang="en">
<head>
<meta charset="utf-8">
<title>Loonie Twoonie Fundraiser</title>
<link rel="stylesheet" href="https://fonts.googleapis.com/css2?family=Montserrat:wght@500;600;700;800;900&display=swap">
<style>
  :root{
    --blue:#1d4496;
    --navy:#142f6e;
    --yellow:#f9c80e;
    --ink:#1c2333;
    --grey:#5b6272;
    --paper:#ffffff;
    --photo-blue:#3f5f9e;
    --photo-warm:#b48c6a;
  }
  *{margin:0;padding:0;box-sizing:border-box}
  html,body{width:849px;height:1200px;overflow:hidden;background:var(--paper)}
  body{font-family:"Montserrat",Arial,sans-serif;color:var(--ink)}
  .flyer{position:relative;width:849px;height:1200px;overflow:hidden;background:var(--paper)}
  .corner-shape{position:absolute;top:0;right:0}
  .title{position:absolute;left:50px;top:48px;font-weight:900;color:var(--blue);font-size:58px;line-height:1.05;letter-spacing:-1px}
  .title .highlight{background:linear-gradient(transparent 60%,var(--yellow) 60%);padding-right:6px}
  .photo{position:absolute;border-radius:50%;border:10px solid var(--yellow)}
  .photo-athlete{left:470px;top:70px;width:330px;height:330px;background:radial-gradient(circle at 45% 40%,var(--photo-warm),var(--photo-blue) 70%)}
  .photo-jersey{left:560px;top:420px;width:250px;height:250px;background:radial-gradient(circle at 50% 45%,#f3f3f3,#9aa3b5 75%)}
  .label{font-weight:600;font-size:22px;color:var(--ink)}
  .big-blue{font-weight:800;color:var(--blue)}
  .travel{position:absolute;left:50px;top:220px}
  .travel .big-blue{font-size:46px;line-height:1.1}
  .tickets{position:absolute;left:50px;top:335px}
  .tickets .big-blue{font-size:32px;line-height:1.2}
  .goal{position:absolute;left:50px;top:470px;width:420px;padding:14px 22px;background:var(--yellow)}
  .goal .label{font-size:20px}
  .goal .amount{font-weight:900;font-size:40px;color:var(--blue);line-height:1.1}
  .prizes{position:absolute;left:50px;top:600px;width:390px}
  .prizes h2{font-weight:800;font-size:26px;color:var(--blue);margin-bottom:14px}
  .prize-list{list-style:none}
  .prize-list li{display:flex;align-items:center;gap:12px;font-size:19px;font-weight:600;margin-bottom:12px}
  .prize-list svg{flex:none}
  .extras{position:absolute;left:490px;top:690px;width:320px}
  .extras h3{font-weight:800;font-size:25px;color:var(--blue);line-height:1.2}
  .extras .sub{font-size:16px;font-weight:700;margin:12px 0 8px}
  .extras p{font-size:15px;color:var(--grey);font-weight:500;line-height:1.45;margin-bottom:8px}
  .thumbs{position:absolute;left:50px;top:900px;width:750px;display:flex;gap:14px}
  .thumb{flex:1;height:110px;border:4px solid var(--blue)}
  .thumb-wood{background:linear-gradient(135deg,#8a5a34,#c9955e)}
  .thumb-safe{background:linear-gradient(135deg,#a11d22,#d9463b)}
  .thumb-latch{background:linear-gradient(135deg,#6d7380,#c6cad2)}
  .thumb-prize{background:linear-gradient(135deg,#2d5aa8,#7fa3dd)}
  .footer{position:absolute;left:0;bottom:0;width:849px;height:170px;background:var(--blue)}
  .footer .accent{position:absolute;left:0;top:-10px;width:849px;height:10px;background:var(--yellow)}
  .draw{position:absolute;left:50px;top:28px;color:#fff}
  .draw .label{color:#fff;font-size:20px}
  .draw .date{font-weight:900;font-size:44px;color:var(--yellow);line-height:1.05}
  .email{position:absolute;left:400px;top:40px;color:#fff;font-size:15px;font-weight:600}
  .brand{position:absolute;right:50px;bottom:36px;display:flex;align-items:center;gap:10px;color:#fff;font-weight:800;font-size:26px}
  .brand .dot{width:18px;height:18px;border-radius:50%;background:var(--yellow)}
</style>
</head>
<body>
<div class="flyer">
  <svg class="corner-shape" width="420" height="470" viewBox="0 0 420 470" aria-hidden="true">
    <polygon points="120,0 420,0 420,470 300,470" fill="var(--blue)"/>
    <polygon points="60,0 120,0 300,470 250,470" fill="var(--yellow)"/>
  </svg>

  <h1 class="title">Loonie Twoonie<br><span class="highlight">Fundraiser</span></h1>

  <div class="photo photo-athlete" role="img" aria-label="Photo of the athlete with a teammate in team jerseys"></div>

  <div class="travel">
    <div class="label">Travel dates:</div>
    <div class="big-blue">July 16-23,2023</div>
  </div>

  <div class="tickets">
    <div class="label">Tickets are</div>
    <div class="big-blue">$2.00 each<br>$5.00 for three</div>
  </div>

  <div class="goal">
    <div class="label">Please help us raise</div>
    <div class="amount">$2000.00</div>
  </div>

  <div class="photo photo-jersey" role="img" aria-label="Photo of the athlete's number 17 jersey"></div>

  <section class="prizes">
    <h2>Raffling off three prizes:</h2>
    <ul class="prize-list">
      <li><svg width="22" height="22" viewBox="0 0 22 22"><circle cx="11" cy="11" r="11" fill="var(--yellow)"/><path d="M6 11l4 4 6-8" stroke="var(--blue)" stroke-width="2.5" fill="none"/></svg>$150.00 Firewood</li>
      <li><svg width="22" height="22" viewBox="0 0 22 22"><circle cx="11" cy="11" r="11" fill="var(--yellow)"/><path d="M6 11l4 4 6-8" stroke="var(--blue)" stroke-width="2.5" fill="none"/></svg>$375.00 Red Safe</li>
      <li><svg width="22" height="22" viewBox="0 0 22 22"><circle cx="11" cy="11" r="11" fill="var(--yellow)"/><path d="M6 11l4 4 6-8" stroke="var(--blue)" stroke-width="2.5" fill="none"/></svg>$300.00 Secure Latch and door knob</li>
      <li><svg width="22" height="22" viewBox="0 0 22 22"><circle cx="11" cy="11" r="11" fill="var(--yellow)"/><path d="M6 11l4 4 6-8" stroke="var(--blue)" stroke-width="2.5" fill="none"/></svg>20 pieces of frozen coho sockeye</li>
    </ul>
  </section>

  <section class="extras">
    <h3>Coffee Provided<br>Baked goods for sale</h3>
    <div class="sub">Items Currently Available to be won:</div>
    <p>Sewn chair/ fan/ and cooler</p>
    <p>1 year Bulkmart Membership</p>
    <p>Fun Outdoor Games. We will have more once June arrives</p>
  </section>

  <div class="thumbs">
    <div class="thumb thumb-wood" role="img" aria-label="Photo of the firewood prize"></div>
    <div class="thumb thumb-safe" role="img" aria-label="Photo of the red safe prize"></div>
    <div class="thumb thumb-latch" role="img" aria-label="Photo of the secure latch and door knob"></div>
    <div class="thumb thumb-prize" role="img" aria-label="Photo of additional raffle items"></div>
  </div>

  <footer class="footer">
    <div class="accent"></div>
    <div class="draw">
      <div class="label">Draw Date:</div>
      <div class="date">July 15,2023<br>11:00am</div>
    </div>
    <div class="email">ETransfer: ashburyfundraiser482@plimvex.com</div>
    <div class="brand"><span class="dot"></span>Team Westline</div>
  </footer>
</div>
</body>
</html>
```